Innovative Australian Importation company in Sustainability space needs beautiful website*

We seek your services to provide a clean, modern we rendered logo for or company Ferntide Commerce Imports Pty Ltd, this will be used in all the usual places however you will aso build us our business cards and our website: ferntidecommerceimports.example

What we do:
We source innovative products that solve problems in the Aeroponics, Hydroponics, Horticultural, Organics and sustainability space. We source our product from all over the world however our cliant base is predominantly in Australia & New Zealand Region.
Our company's mission is to help retail businesses by providing high-quality products at a competitive price for everyday people to produce healthy sustainable consumables from home, making it easy for the end-user to become more self-sufficient with while remaining environmentally friendly.

Target Market(s)

Aeroponics, Hydroponics, Horticultural, Organics and sustainability space.

Industry/Entity Type

Wholesale

Contact Information for Business Card

We would like these to be very modern and glossy possibly an embosed logo or rounded edges, a little smaller than the traditional?

Logo Text

Ferntide Commerce Imports

Coding

Coded - Design and coding required

Number of Pages Required

1 page

Colors
0355a3

Requirements
Must have
• The websit is bit of a landing page that will provide some minor information on our imported products. and qualify resellers ( Our target Market) from retail clients (the end-user) and provide a private store and check out for our trade customers. (not for Reatil)
Abillity to set up a trade account (must have our approval befor being granted access to shop.)
the abillity to for OEM's and International wholsalers register intrest.
The abillity to register/inquire about our produtc lines for Retailer.
The abillity to provide the end-user a list of resellers.
The ability for promo video
Nice to have
• .
Should not have
• Logo high gloss, 3d rendered

```html
<!DOCTYPE html>
<html lang="en">
<head>
<meta charset="utf-8">
<title>Ferntide Commerce Imports</title>
<link href="https://fonts.googleapis.com/css2?family=Montserrat:wght@400;500;600;700;800&display=swap" rel="stylesheet">
<style>
:root{
  --brand-blue:#24399c;
  --purple:#3c1d7c;
  --purple-dark:#1d0f3e;
  --purple-mid:#4a2389;
  --red:#e1173f;
  --nav-red:#e0324f;
  --ink:#333;
  --grey-text:#555;
  --grey-light:#9a9a9a;
  --tile:#efefef;
  --link-blue:#2c4ba3;
  --contact-top:#1d4fa5;
  --contact-bottom:#1a1d48;
  --footer:#121212;
  --white:#fff;
}
*{margin:0;padding:0;box-sizing:border-box}
html,body{width:1200px;height:3530px;overflow:hidden;background:var(--white)}
body{font-family:'Montserrat',sans-serif;color:var(--ink);position:relative}
.abs{position:absolute}
h1,h2,h3{font-weight:inherit}

/* header */
.brand{left:143px;top:20px}
.brand-name{font-size:28px;font-weight:700;color:var(--brand-blue);letter-spacing:-.4px;line-height:36px}
.brand-tag{font-size:13px;color:var(--grey-text)}
.btn-top{top:30px;height:38px;display:flex;align-items:center;justify-content:center;gap:9px;color:var(--white);font-size:12px;text-transform:uppercase;border-radius:2px}
.btn-trade{left:621px;width:152px;background:#2a4ea5}
.btn-login{left:782px;width:87px;background:var(--purple)}
.btn-register{left:878px;width:111px;background:var(--purple)}
.btn-cart{left:1015px;width:40px;background:var(--red)}
.cart-count{left:1006px;top:27px;width:18px;height:18px;border-radius:50%;background:#111;color:#fff;font-size:9px;display:flex;align-items:center;justify-content:center}

.main-nav{left:0;top:96px;width:1200px;height:42px;background:linear-gradient(#f3f3f3,#e6e6e6);border-top:1px solid #ddd}
.main-nav ul{list-style:none;display:flex;position:absolute;left:174px;top:13px;font-size:13px;text-transform:uppercase;color:#222}
.main-nav li.active{color:var(--nav-red)}

/* hero */
.hero{left:0;top:138px;width:1200px;height:572px;
  background:
    radial-gradient(ellipse 260px 200px at 600px 110px,rgba(150,200,90,.9),rgba(150,200,90,0)),
    radial-gradient(ellipse 420px 300px at 880px 380px,rgba(214,160,120,.85),rgba(214,160,120,0)),
    radial-gradient(ellipse 500px 160px at 650px 30px,rgba(225,232,228,.8),rgba(225,232,228,0)),
    linear-gradient(100deg,#2e6a1c 0%,#5e9a34 30%,#7aa848 50%,#a48a62 72%,#6d8aa0 100%)}
.hero-title{left:0;top:345px;width:1200px;text-align:center;font-size:46px;font-weight:800;color:var(--white);text-shadow:0 2px 6px rgba(0,0,0,.6)}
.btn-video{left:524px;top:407px;width:151px;height:38px;background:var(--red);color:var(--white);font-size:15px;font-weight:600;display:flex;align-items:center;justify-content:center;gap:9px;text-transform:uppercase;border-radius:2px}
.hero-curve{left:0;top:610px}

/* mission */
.mission-title{left:143px;top:784px;font-size:31px;font-weight:700;color:var(--purple)}
.mission-text{left:144px;top:834px;width:445px;font-size:16px;line-height:28.7px;color:#333}
.mission-photo{left:616px;top:790px;width:440px;height:188px;
  background:
    radial-gradient(ellipse 140px 90px at 180px 90px,rgba(120,180,70,.9),rgba(120,180,70,0)),
    radial-gradient(ellipse 120px 80px at 360px 140px,rgba(80,150,50,.9),rgba(80,150,50,0)),
    linear-gradient(120deg,#b89c86 0%,#e6e2dc 35%,#8fa77c 60%,#3c4a34 100%)}
.rule{left:0;width:1200px;height:1px;background:#cfcfcf}

/* clients */
.client-sub{left:0;top:1133px;width:1200px;text-align:center;font-size:31px;font-weight:600;color:var(--grey-text)}
.client-main{left:0;top:1182px;width:1200px;text-align:center;font-size:48px;font-weight:700;color:var(--grey-light)}
.sectors{left:0;top:1262px;width:1200px;height:238px;display:flex;gap:2px}
.sector{flex:1;position:relative}
.sector::after{content:"";position:absolute;left:0;right:0;bottom:0;height:80px;background:linear-gradient(rgba(0,0,0,0),rgba(0,0,0,.35))}
.sector span{position:absolute;left:0;right:0;bottom:12px;text-align:center;color:var(--white);font-size:20px;font-weight:600;text-shadow:0 1px 3px rgba(0,0,0,.5);z-index:1}
.s1{background:radial-gradient(ellipse at 40% 35%,#a6e05a,#5a9e2a 55%,#2f6418)}
.s2{background:radial-gradient(ellipse at 70% 20%,#f0e6a8,#b4d25c 40%,#5a8e26 80%)}
.s3{background:linear-gradient(#d9dde0 0%,#c8507a 35%,#6e8a3c 70%,#3e4a3a 100%)}
.s4{background:linear-gradient(#4d7fb8 0%,#b8cde0 35%,#c89a5e 48%,#5e7a2e 65%,#35501a 100%)}
.s5{background:linear-gradient(#e8eae8 0%,#aeb6ae 40%,#5c6a4e 70%,#3a3428 100%)}

/* products */
.products{left:0;top:1502px;width:1200px;height:561px;background:linear-gradient(var(--purple-dark),var(--purple-mid))}
.section-title{left:0;width:1200px;text-align:center;font-size:32px;font-weight:700}
.products .section-title{top:85px;color:var(--white)}
.product{top:140px;width:210px;color:var(--white)}
.product-photo{width:210px;height:185px}
.p1{background:radial-gradient(ellipse 90px 80px at 50% 45%,#b8c9a8,#e8ece4 70%,#fafafa)}
.p2{background:radial-gradient(ellipse 75px 40px at 50% 55%,#1c1c1c,#3a3a3a 45%,#f4f4f4 100%)}
.p3{background:radial-gradient(ellipse 20px 30px at 50% 30%,#2448c4,#8aa0d8 60%,rgba(255,255,255,0) 100%),radial-gradient(ellipse 90px 75px at 50% 55%,#cfd2d4,#ffffff 80%)}
.p4{background:radial-gradient(ellipse 70px 60px at 50% 70%,#3a3a3a,rgba(58,58,58,0)),linear-gradient(#6f8c5a 0%,#d7dad6 40%,#b8bdb6 100%)}
.product-name{font-size:16px;font-weight:500;margin-top:13px}
.product-desc{font-size:10px;line-height:17.5px;color:#b9afcf;margin-top:6px}
.btn-outline{display:inline-flex;align-items:center;justify-content:center;width:96px;height:34px;border:1px solid #a99cc6;color:#cfc6e0;font-size:10px;text-transform:uppercase;margin-top:17px}
.arrow{width:26px;height:36px}

/* resellers */
.resellers-title{top:2136px;color:var(--purple)}
.reseller{top:2200px;width:210px;height:158px;background:var(--tile);display:flex;align-items:center;justify-content:center;gap:8px;font-size:20px;font-weight:700;color:#333}
.reseller i{display:block;width:16px;height:16px;border-radius:50%;background:#333}

/* news */
.news-title{top:2513px;color:var(--purple)}
.news-item{top:2570px;width:433px}
.news-photo{width:433px;height:192px}
.n1{background:radial-gradient(ellipse 160px 40px at 50% 60%,#6fa442,rgba(111,164,66,0)),linear-gradient(#f4f4f2,#dfe2dc 60%,#eeeeec)}
.n2{background:radial-gradient(ellipse 110px 80px at 65% 30%,#6fa048,rgba(111,160,72,0)),radial-gradient(ellipse 90px 60px at 78% 75%,#c48e6c,rgba(196,142,108,0)),linear-gradient(110deg,#8ab8d6,#5e8e6a 45%,#324632)}
.news-head{font-size:18px;font-weight:400;line-height:27px;color:var(--link-blue);margin-top:10px}
.news-date{font-size:11px;color:#333;margin-top:6px}
.btn-view{left:555px;top:2870px;width:89px;height:38px;background:var(--link-blue);color:var(--white);font-size:11px;text-transform:uppercase;display:flex;align-items:center;justify-content:center}

/* contact */
.contact{left:0;top:2988px;width:1200px;height:444px;background:linear-gradient(var(--contact-top),var(--contact-bottom))}
.contact .section-title{top:80px;color:var(--white)}
.field{top:132px;width:218px;height:40px;background:var(--white);border-radius:2px;font-size:13px;color:#555;padding:12px 14px}
.field-select{display:flex;justify-content:space-between;align-items:center;padding:0 14px}
.field-message{left:143px;top:188px;width:913px;height:112px;background:var(--white);border-radius:2px;font-size:13px;color:#555;padding:12px 14px}
.btn-submit{left:555px;top:317px;width:89px;height:38px;background:var(--red);color:var(--white);font-size:11px;text-transform:uppercase;display:flex;align-items:center;justify-content:center;border-radius:2px}

/* footer */
.site-footer{left:0;top:3432px;width:1200px;height:98px;background:var(--footer)}
.footer-links{left:143px;top:30px;font-size:10px;color:#6f7fc6}
.footer-links b{font-weight:400;color:#666;margin:0 7px}
.copyright{left:143px;top:62px;font-size:10px;color:#6f7fc6}
.social{top:44px;font-size:11px;color:#888;display:flex;gap:18px;left:925px}
</style>
</head>
<body>

<header>
  <div class="abs brand">
    <div class="brand-name">Ferntide Commerce Imports</div>
    <div class="brand-tag">Connecting your Business to a world of products</div>
  </div>
  <a class="abs btn-top btn-trade"><svg width="13" height="13" viewBox="0 0 13 13"><circle cx="6.5" cy="4" r="3" fill="#fff"/><path d="M1 13c0-4 2.5-5 5.5-5s5.5 1 5.5 5z" fill="#fff"/></svg>Trade account</a>
  <a class="abs btn-top btn-login"><svg width="13" height="12" viewBox="0 0 13 12"><path d="M0 4.5h5V2l4 4-4 4V7.5H0z" fill="#fff"/><path d="M8 1h4v10H8" stroke="#fff" stroke-width="1.6" fill="none"/></svg>Login</a>
  <a class="abs btn-top btn-register"><svg width="13" height="13" viewBox="0 0 13 13"><rect x="1" y="2" width="10" height="10" stroke="#fff" stroke-width="1.6" fill="none"/><path d="M5 8l1-3 6-5 1 1-5 6z" fill="#fff"/></svg>Register</a>
  <a class="abs btn-top btn-cart"><svg width="15" height="13" viewBox="0 0 15 13"><path d="M0 1h3l2 7h8l2-6H4" fill="#fff"/><circle cx="6" cy="11" r="1.5" fill="#fff"/><circle cx="12" cy="11" r="1.5" fill="#fff"/></svg></a>
  <div class="abs cart-count">0</div>
  <nav class="abs main-nav">
    <ul>
      <li class="active" style="width:101px">Home</li>
      <li style="width:127px">About us</li>
      <li style="width:124px">Services</li>
      <li style="width:132px">Products</li>
      <li style="width:100px">News</li>
      <li style="width:96px">Blog</li>
      <li style="width:142px">Contact us</li>
      <li>FAQ</li>
    </ul>
  </nav>
</header>

<section>
  <div class="abs hero" role="img" aria-label="Hands holding a lettuce seedling in a net pot with roots above a hydroponic growing bed"></div>
  <h1 class="abs hero-title">CRAS SOLLICITUDIN CURSUS</h1>
  <a class="abs btn-video"><svg width="14" height="14" viewBox="0 0 14 14"><circle cx="7" cy="7" r="7" fill="#fff"/><path d="M5 4l5 3-5 3z" fill="#e1173f"/></svg>Play video</a>
  <svg class="abs hero-curve" width="1200" height="100" viewBox="0 0 1200 100">
    <defs><linearGradient id="band" x1="0" x2="1"><stop offset="0" stop-color="#2b2c8f"/><stop offset=".5" stop-color="#3a2a8e"/><stop offset="1" stop-color="#2b47a8"/></linearGradient></defs>
    <path d="M0 5 Q600 160 1200 0 L1200 100 L0 100Z" fill="url(#band)"/>
    <path d="M0 12 Q600 185 1200 8 L1200 100 L0 100Z" fill="#fff"/>
  </svg>
</section>

<section>
  <h2 class="abs mission-title">Our company's mission...</h2>
  <p class="abs mission-text">...is to help retail businesses by providing high-quality products at a competitive price for everyday people to produce healthy sustainable consumables from home, making it easy for the end-user to become more self-sufficient while remaining environmentally friendly.</p>
  <div class="abs mission-photo" role="img" aria-label="Hand lifting a young leafy plant in a net pot from a hydroponic tray"></div>
</section>

<div class="abs rule" style="top:1059px"></div>

<section>
  <h2 class="abs client-sub">Our client base is predominantly in</h2>
  <p class="abs client-main">Australia &amp; New Zealand Region on...</p>
  <div class="abs sectors">
    <div class="sector s1" role="img" aria-label="Hands harvesting lettuce heads"><span>Aeroponics</span></div>
    <div class="sector s2" role="img" aria-label="Rows of hydroponic lettuce"><span>Hydroponics</span></div>
    <div class="sector s3" role="img" aria-label="Flower nursery greenhouse"><span>Horticultural</span></div>
    <div class="sector s4" role="img" aria-label="Tractor working a crop field"><span>Organics</span></div>
    <div class="sector s5" role="img" aria-label="Sprinkler over young crop rows"><span>Sustainability Space</span></div>
  </div>
</section>

<section class="abs products">
  <h2 class="abs section-title">Our Products</h2>
  <svg class="abs arrow" style="left:52px;top:218px" viewBox="0 0 26 36"><path d="M20 4L7 18l13 14" stroke="#fff" stroke-width="4" fill="none"/></svg>
  <svg class="abs arrow" style="left:1122px;top:218px" viewBox="0 0 26 36"><path d="M6 4l13 14L6 32" stroke="#fff" stroke-width="4" fill="none"/></svg>
  <article class="abs product" style="left:143px">
    <div class="product-photo p1" role="img" aria-label="Vertical aeroponic grow towers"></div>
    <h3 class="product-name">Proin eget</h3>
    <p class="product-desc">Etiam vel massa elementum, bibendum tellus venenatis, feugiat massa. Curabi-tur venenatis lacinia ornare.</p>
    <a class="btn-outline">Read more</a>
  </article>
  <article class="abs product" style="left:378px">
    <div class="product-photo p2" role="img" aria-label="Stack of black foam plant collars"></div>
    <h3 class="product-name">Fusce eget</h3>
    <p class="product-desc">Etiam vel massa elementum, bibendum tellus venenatis, feugiat massa. Curabi-tur venenatis lacinia ornare.</p>
    <a class="btn-outline">Read more</a>
  </article>
  <article class="abs product" style="left:612px">
    <div class="product-photo p3" role="img" aria-label="Tower garden kit with pump"></div>
    <h3 class="product-name">Phasellus conseq</h3>
    <p class="product-desc">Etiam vel massa elementum, bibendum tellus venenatis, feugiat massa. Curabi-tur venenatis lacinia ornare.</p>
    <a class="btn-outline">Read more</a>
  </article>
  <article class="abs product" style="left:846px">
    <div class="product-photo p4" role="img" aria-label="Hydroponic channels with seedlings"></div>
    <h3 class="product-name">Aliquam consect</h3>
    <p class="product-desc">Etiam vel massa elementum, bibendum tellus venenatis, feugiat massa. Curabi-tur venenatis lacinia ornare.</p>
    <a class="btn-outline">Read more</a>
  </article>
</section>

<section>
  <h2 class="abs section-title resellers-title">Qualify Resellers</h2>
  <svg class="abs arrow" style="left:52px;top:2261px" viewBox="0 0 26 36"><path d="M20 4L7 18l13 14" stroke="#777" stroke-width="3" fill="none"/></svg>
  <svg class="abs arrow" style="left:1122px;top:2261px" viewBox="0 0 26 36"><path d="M6 4l13 14L6 32" stroke="#777" stroke-width="3" fill="none"/></svg>
  <div class="abs reseller" style="left:143px"><i></i>Tidewell</div>
  <div class="abs reseller" style="left:378px">Corvane</div>
  <div class="abs reseller" style="left:612px">Saltreach</div>
  <div class="abs reseller" style="left:846px">Marlow &amp; Pine</div>
</section>

<div class="abs rule" style="top:2440px"></div>

<section>
  <h2 class="abs section-title news-title">News</h2>
  <article class="abs news-item" style="left:143px">
    <div class="news-photo n1" role="img" aria-label="Young leafy seedlings on a white surface"></div>
    <h3 class="news-head">Praesent iaculis faucibus urna sit amet lacinia consequat sagittis nisi suscipit feugiat.</h3>
    <p class="news-date">17 August, 2020</p>
  </article>
  <article class="abs news-item" style="left:623px">
    <div class="news-photo n2" role="img" aria-label="Hand holding a seedling in a net pot"></div>
    <h3 class="news-head">Maecenas tortor accumsan qua varius imperdiet vel eget elit</h3>
    <p class="news-date">17 August, 2020</p>
  </article>
  <a class="abs btn-view">View all</a>
</section>

<section class="abs contact">
  <h2 class="abs section-title">Contact us</h2>
  <div class="abs field" style="left:143px">Name</div>
  <div class="abs field" style="left:375px">Email</div>
  <div class="abs field" style="left:607px">Phone</div>
  <div class="abs field field-select" style="left:838px">Service for<svg width="10" height="6" viewBox="0 0 10 6"><path d="M0 0h10L5 6z" fill="#333"/></svg></div>
  <div class="abs field-message">Message</div>
  <a class="abs btn-submit">Submit</a>
</section>

<footer class="abs site-footer">
  <p class="abs footer-links">Home<b>|</b>About Us<b>|</b>Services<b>|</b>Products<b>|</b>News<b>|</b>Blog<b>|</b>Contact Us<b>|</b>FAQ</p>
  <p class="abs copyright">Copyright © 2020 Ferntide Commerce Imports. All rights reserved.</p>
  <div class="abs social"><span>Linkmesh</span><span>Chirpline</span><span>Reelhub</span></div>
</footer>

</body>
</html>
```